Sports and Remedial Massage, Varlow Technique

sports and remedial massage and Varlow technique.
Varlow technique consists of a light touch on certain trigger areas that encourage muscles to relax and reform to a natural way.
I don't have a company name, I just use my name. im unsure weather to have my name or just what I do as a title on the cards.
I like the idea of a muscle skeleton maybe with a few dots marking points.
my colour theme is green but not to dark, still vibrant. maybe with a white or black...
I would like something mutual that both genders will look at and be comfortable keeping that card in their wallet etc.
I have a growing clientele that ranges from farm station hands, sports teams and general public.
please note the images attached are just ideas and colours.
thankyou

Industry/Entity Type

Massage

Contact Information for Business Card

Corinne Whitlam
member of the GRPA #0512389476
Ph: 07 4981 2063, Mob: 0471936204, email: corinne.whitlam4@tramvex.com.
shop 5 41-43 Brindabell st, Tarrant Ridge, QLD, 4829

Colors
9bcb3c
acd037
33b7a4

Requirements
Must have
• Green!!!!!

```html
<!DOCTYPE html>
<html lang="en">
<head>
<meta charset="utf-8">
<title>Corinne Whitlam – Business Card</title>
<link rel="stylesheet" href="https://fonts.googleapis.com/css2?family=Marcellus+SC&family=Questrial&display=swap">
<style>
  :root {
    --page-bg: #e9e9e6;
    --green-deep: #0b6b2f;
    --green-mid: #13913f;
    --green-bright: #22b24f;
    --green-glow: #3fe07a;
    --muscle-red: #c9604a;
    --muscle-light: #e7b9a0;
    --muscle-dark: #a94a38;
    --figure-grey: #5b6560;
    --text-light: #f2f7f3;
    --card-shadow: rgba(0, 0, 0, 0.25);
  }
  * { box-sizing: border-box; margin: 0; padding: 0; }
  html, body {
    width: 1200px;
    height: 900px;
    overflow: hidden;
    background: var(--page-bg);
  }
  .sheet {
    width: 1200px;
    height: 900px;
    display: flex;
    flex-direction: column;
    align-items: center;
    justify-content: center;
    gap: 40px;
  }
  .card {
    position: relative;
    width: 700px;
    height: 400px;
    overflow: hidden;
    box-shadow: 0 6px 18px var(--card-shadow);
  }

  /* Front side */
  .card-front {
    background: radial-gradient(ellipse 80% 90% at 40% 10%, var(--green-bright) 0%, var(--green-mid) 40%, var(--green-deep) 90%);
  }
  .anatomy-illustration {
    position: absolute;
    left: 0;
    top: 0;
    width: 300px;
    height: 330px;
    border-bottom-right-radius: 55% 45%;
    background: linear-gradient(160deg, var(--muscle-light) 0%, var(--muscle-red) 50%, var(--muscle-dark) 100%);
  }
  .contact-block {
    position: absolute;
    right: 34px;
    top: 96px;
    width: 360px;
    text-align: right;
    color: var(--text-light);
    font-family: "Questrial", sans-serif;
    font-size: 13.5px;
    letter-spacing: 0.12em;
    line-height: 1.55;
  }
  .holder-name {
    font-family: "Marcellus SC", serif;
    font-size: 21px;
    letter-spacing: 0.14em;
    font-weight: 400;
    margin-bottom: 2px;
  }
  .membership { margin-bottom: 26px; }
  .address { margin-bottom: 26px; }
  .contact-line {
    display: flex;
    justify-content: flex-end;
    align-items: center;
    gap: 10px;
  }
  .contact-line svg {
    width: 13px;
    height: 13px;
    fill: var(--text-light);
    flex: none;
  }

  /* Back side */
  .card-back {
    background: radial-gradient(ellipse at 50% 45%, var(--green-glow) 0%, var(--green-mid) 35%, var(--green-deep) 85%);
  }
  .stretch-sequence {
    position: absolute;
    left: 50%;
    top: 50%;
    width: 250px;
    height: 62px;
    transform: translate(-50%, -60%);
    border-radius: 6px;
    background: linear-gradient(90deg, var(--figure-grey) 0%, #3c4a42 60%, #1f5a36 100%);
    opacity: 0.75;
  }
</style>
</head>
<body>
<main class="sheet">

  <section class="card card-front" aria-label="Card front">
    <div class="anatomy-illustration" role="img" aria-label="Anatomical illustration of the back and shoulder muscles"></div>

    <div class="contact-block">
      <h1 class="holder-name">Corinne Whitlam</h1>
      <p class="membership">member of the GRPA #0512389476</p>
      <p class="address">shop 5 41-43 Brindabell<br>st, Tarrant Ridge, QLD, 4829</p>
      <p class="contact-line">07 4981 2063
        <svg viewBox="0 0 16 16" aria-hidden="true"><path d="M3 1h3l1.5 4-2 1.3a9 9 0 0 0 4.2 4.2L11 8.5l4 1.5v3c0 1-1 2-2 2A12 12 0 0 1 1 3c0-1 1-2 2-2z"/></svg>
      </p>
      <p class="contact-line">0471936204
        <svg viewBox="0 0 16 16" aria-hidden="true"><path d="M4 0h8a1 1 0 0 1 1 1v14a1 1 0 0 1-1 1H4a1 1 0 0 1-1-1V1a1 1 0 0 1 1-1zm1 2v10h6V2zm3 11a1 1 0 1 0 0 2 1 1 0 0 0 0-2z"/></svg>
      </p>
      <p class="contact-line">corinne.whitlam4@tramvex.com
        <svg viewBox="0 0 16 16" aria-hidden="true"><path d="M1 3h14v10H1zm1.5 1.2V12h11V4.2L8 8.5z M2.8 4 8 7.6 13.2 4z"/></svg>
      </p>
    </div>
  </section>

  <section class="card card-back" aria-label="Card back">
    <div class="stretch-sequence" role="img" aria-label="Row of small silhouette figures moving through a stretch sequence"></div>
  </section>

</main>
</body>
</html>
```